Vela Habitat Real estate Costa del sol

we need a website for our Company based in Costa del sol, Spain. We sell properties on the spanish coast that is called costa del sol. We are concentrating on exclusive properties and would like the webdesign to show this. In our website we want to have area descriptions of the different areas we sell our Products. We will also implement a searchable database delivered by a third part where all properties for sale in Spain are listed. When looking into the designs we would like our main page to have a overview of the coast where the different areas are shown. Have a look at brightlomaview.com or ourtesa.com to see. The webpage will be presented in 4 languages, English, spanish, Swedish and norwegian, and shall of course also be prepared for social medias. We want an easy Contemporary design but still with an exclusive feeling!
Target Market(s)
Scandinavian and North european Citizens wants to buy a property in Spain
Industry/Entity Type
Real Estate
Number of Pages Required
5+ page
Look and feel

```html
<!DOCTYPE html>
<html lang="en">
<head>
<meta charset="utf-8">
<title>Vela Habitat – Costa del Sol Real Estate</title>
<link href="https://fonts.googleapis.com/css2?family=Open+Sans:wght@400;600;700&display=swap" rel="stylesheet">
<style>
:root{
  --navy:#101a3d;
  --navy-deep:#0b1330;
  --orange:#ff5a1f;
  --ink:#222633;
  --muted:#7a7f8c;
  --line:#e3e5ea;
  --light:#f4f4f5;
  --white:#ffffff;
}
*{box-sizing:border-box;margin:0;padding:0}
html,body{width:1200px;height:3719px;overflow:hidden}
body{font-family:"Open Sans",Arial,sans-serif;color:var(--ink);background:var(--white);position:relative;font-size:13px}
.abs{position:absolute}
section,header,footer{position:absolute;left:0;width:1200px}

/* top bar */
.topbar{top:0;height:30px;background:var(--navy);color:#cfd3df;font-size:11px}
.topbar .lang{left:156px;top:8px}
.topbar .contact{top:8px;display:flex;gap:6px;align-items:center;white-space:nowrap}
.topbar .socials{right:169px;top:0;display:flex;height:30px}
.topbar .socials span{width:40px;height:30px;border-left:1px solid #26305a;display:flex;align-items:center;justify-content:center}
.topbar .socials span i{width:11px;height:11px;background:#cfd3df;display:block;border-radius:2px}
.topbar .socials span.on i{background:var(--orange)}

/* header */
.site-header{top:30px;height:89px;background:var(--white)}
.brand{left:156px;top:30px;display:flex;align-items:center;gap:10px;font-size:24px;font-weight:600;color:var(--navy)}
.brand .mark{width:26px;height:26px;border:3px solid var(--navy)}
.nav{left:449px;top:37px;display:flex;gap:27px;font-size:11px;font-weight:600;color:var(--navy);text-transform:uppercase}
.nav .active{color:var(--orange);border-bottom:2px solid var(--orange);padding-bottom:6px}
.nav-search{left:1030px;top:35px}

/* hero */
.hero{top:119px;height:483px;background:linear-gradient(90deg,#3c4a33 0%,#5a6251 35%,#4a4a48 60%,#3a3836 100%)}
.hero .floor{left:0;top:330px;width:1200px;height:153px;background:linear-gradient(#56504a,#2e2a27)}
.search-tabs{left:156px;top:136px;display:flex}
.search-tabs span{width:42px;height:30px;background:#e9e9ea;display:flex;align-items:center;justify-content:center}
.search-tabs span.on{background:var(--orange)}
.search-tabs i{width:12px;height:12px;background:#555;display:block}
.search-tabs .on i{background:#fff}
.search-panel{left:156px;top:166px;width:885px;height:183px;background:rgba(255,255,255,.82)}
.select{top:24px;height:37px;border:1px solid #c9cbd0;background:#fff;font-size:11px;color:#555;padding:10px 12px}
.select:after{content:"";position:absolute;right:12px;top:14px;width:6px;height:6px;border-right:1.5px solid #777;border-bottom:1.5px solid #777;transform:rotate(45deg)}
.range{top:88px;font-size:11px;font-weight:700;color:var(--ink)}
.range .val{position:absolute;right:0;top:0;font-weight:600}
.range .track{position:absolute;left:0;right:0;top:22px;height:2px;background:var(--orange)}
.range .track:before,.range .track:after{content:"";position:absolute;top:-5px;width:12px;height:12px;border-radius:50%;background:var(--orange)}
.range .track:before{left:-4px}.range .track:after{right:-4px}
.btn-search{left:761px;top:149px;width:124px;height:34px;background:var(--orange);color:#fff;font-size:11px;font-weight:700;display:flex;align-items:center;justify-content:center;gap:6px}

/* categories */
.categories{top:602px;height:360px}
.cat{top:92px;width:204px;height:211px;border:1px solid var(--line);background:#fff;text-align:center}
.cat.featured{border-color:var(--navy);box-shadow:0 2px 10px rgba(0,0,0,.08)}
.cat .icon{position:absolute;left:65px;top:-37px;width:74px;height:74px;border-radius:50%;background:#fff;border:1px solid var(--line);display:flex;align-items:center;justify-content:center}
.cat.featured .icon{background:var(--navy);border-color:var(--navy)}
.cat h3{margin-top:58px;font-size:14px;font-weight:600;color:var(--navy)}
.cat .bar{width:40px;height:2px;background:var(--navy);margin:8px auto 12px}
.cat p{font-size:11px;color:var(--muted);line-height:1.45;padding:0 22px}
.cat a{display:block;margin-top:16px;font-size:11px;font-weight:700;color:var(--navy);text-decoration:none}

/* welcome */
.welcome{top:962px;height:317px;background:#f8f8f8}
.welcome .photo{left:612px;top:0;width:588px;height:317px;background:linear-gradient(180deg,#d7d2c8 0%,#eae8e4 40%,#dcd9d4 75%,#b89a78 100%)}
.welcome h2{left:156px;top:50px;width:440px;font-size:21px;font-weight:700;line-height:1.35;color:var(--navy)}
.welcome h2 em{font-style:normal;color:var(--orange)}
.welcome p{left:156px;top:120px;width:420px;font-size:11px;color:#555;line-height:1.55}
.features{left:156px;top:202px;display:flex;gap:30px;font-size:12px;color:#444;align-items:center}
.features span{display:flex;gap:10px;align-items:center}
.explore{left:156px;top:248px;font-size:11px;color:var(--orange);font-weight:600}

/* featured */
.featured-sec{top:1279px;height:625px}
.sec-title{font-size:19px;font-weight:700;color:var(--navy)}
.sec-title em{font-style:normal;color:var(--orange)}
.featured-sec .sec-title{left:156px;top:52px}
.featured-sec .title-line{left:156px;top:84px;width:888px;height:1px;background:var(--line)}
.featured-sec .title-line:before{content:"";position:absolute;left:0;top:-1px;width:160px;height:3px;background:var(--navy)}
.arrows{left:988px;top:64px;display:flex;gap:12px}
.prop{top:114px;width:279px;height:387px;border:1px solid var(--line);background:#fff}
.prop.raised{box-shadow:0 4px 16px rgba(0,0,0,.18);border-color:#d5d7dc}
.prop .photo{height:149px}
.prop .tag{position:absolute;right:0;top:128px;width:50px;height:21px;color:#fff;font-size:10px;font-weight:700;text-align:center;line-height:21px}
.prop h4{margin:22px 24px 0;font-size:14px;font-weight:700;color:var(--navy)}
.prop .price{margin:2px 24px 0;font-size:14px;font-weight:700;color:var(--orange)}
.prop p{margin:14px 24px 0;font-size:11px;color:var(--muted);line-height:1.45}
.prop ul{list-style:none;margin:16px 24px 0;font-size:11px;font-weight:700;color:var(--navy)}
.prop li{margin-bottom:5px;padding-left:16px;position:relative}
.prop li:before{content:"";position:absolute;left:0;top:4px;width:5px;height:5px;border-right:1.5px solid var(--orange);border-top:1.5px solid var(--orange);transform:rotate(45deg)}
.btn-view{left:535px;top:558px;width:130px;height:32px;background:var(--orange);color:#fff;font-size:11px;font-weight:600;display:flex;align-items:center;justify-content:center}

/* stats */
.stats{top:1904px;height:198px;background:var(--light)}
.stat{top:50px;width:200px;text-align:center}
.stat .u{width:54px;height:2px;background:var(--orange);margin:8px auto 14px}
.stat small{display:block;font-size:11px;color:#666;text-transform:uppercase}
.stat b{display:block;font-size:18px;color:var(--navy);margin-top:4px}
.stat-div{top:48px;width:1px;height:108px;background:#d9dbe0}

/* work */
.work{top:2102px;height:608px}
.work .sec-title{left:0;width:1200px;text-align:center;top:46px}
.work .sub{left:300px;width:600px;top:98px;text-align:center;font-size:11px;font-style:italic;color:#8a8e98;line-height:1.6}
.filters{left:0;width:1200px;top:158px;display:flex;justify-content:center;gap:34px;font-size:11px;color:#444}
.filters .on{color:var(--orange);border-bottom:2px solid var(--orange);padding-bottom:4px}
.tile{width:300px;height:200px}
.tile.active{box-shadow:inset 0 0 0 4px #fff,inset 0 0 0 6px var(--orange)}

/* blogs */
.blogs{top:2710px;height:433px}
.blogs .sec-title{left:0;width:1200px;text-align:center;top:50px}
.post-img{top:111px;width:203px;height:253px}
.post-date{top:111px;width:40px;height:44px;background:var(--orange);color:#fff;font-weight:700;font-size:13px;text-align:center;line-height:44px}
.post-text{top:111px;width:211px}
.post-text h4{font-size:14px;font-weight:600;color:var(--navy);line-height:1.3}
.post-text .d{margin-top:12px;padding-top:10px;border-top:1px solid var(--line);font-size:10px;color:#999}
.post-text p{margin-top:14px;font-size:11px;color:#666;line-height:1.5}
.post-text a{display:block;margin-top:18px;font-size:11px;color:var(--orange);font-weight:600}

/* cta */
.cta{top:3143px;height:112px;background:var(--navy)}
.cta svg{position:absolute;left:0;top:0}
.cta h3{left:156px;top:32px;font-size:15px;font-weight:700;color:#fff;text-transform:uppercase}
.cta p{left:156px;top:54px;font-size:13px;color:#fff}
.btn{height:32px;font-size:12px;color:#fff;display:flex;align-items:center;justify-content:center}
.btn-start{left:778px;top:45px;width:122px;background:var(--orange)}
.btn-contact{left:925px;top:45px;width:119px;border:1px solid #fff}

/* contact */
.contact{top:3255px;height:402px;background:linear-gradient(90deg,#1d2024 0%,#2c2e31 40%,#3a3b3c 70%,#24282b 100%)}
.panel{left:156px;top:0;width:303px;height:402px;background:rgba(12,14,18,.55);color:#e4e6ea;padding:74px 40px 0 40px}
.panel h4{font-size:14px;font-weight:600;color:#fff}
.panel .rule{height:1px;background:#6b6f77;margin:10px 0 12px}
.panel .addr{font-size:11px;line-height:1.45;color:#c9ccd2}
.panel h5{margin-top:14px;font-size:12px;font-weight:600;color:#fff}
.panel .call{font-size:17px;margin-top:4px;color:#fff;white-space:nowrap}
.panel .mail{font-size:11px;color:var(--orange)}
.panel .soc{display:flex;gap:3px;margin-top:8px}
.panel .soc i{width:17px;height:17px;background:#2a6fcf;display:block}
.form{left:598px;top:0;width:446px;height:402px;border-left:1px solid rgba(255,255,255,.25)}
.form label{position:absolute;font-size:11px;color:#d7d9de}
.form .field{position:absolute;border:1px solid #8b8f96;background:rgba(0,0,0,.15)}
.form .note{position:absolute;left:14px;top:260px;font-size:11px;color:#d7d9de}
.form .note b{color:var(--orange);font-weight:600}
.btn-send{position:absolute;left:14px;top:293px;width:107px;height:27px;border:1px solid #d7d9de;color:#fff;font-size:11px;display:flex;align-items:center;justify-content:center;gap:6px}

/* footer */
.site-footer{top:3657px;height:62px;background:var(--navy-deep);font-size:10px;color:#9aa0b0}
.site-footer .copy{left:156px;top:24px}
.site-footer .links{left:538px;top:24px}
.to-top{left:1004px;top:15px;width:32px;height:32px;border-radius:50%;background:var(--orange);display:flex;align-items:center;justify-content:center}
</style>
</head>
<body>

<header class="topbar">
  <div class="abs lang">Language &#9662;</div>
  <div class="abs contact" style="left:533px">
    <svg width="12" height="9" viewBox="0 0 12 9"><rect x=".5" y=".5" width="11" height="8" fill="none" stroke="#cfd3df"/><path d="M.5 .5l5.5 4.5 5.5-4.5" fill="none" stroke="#cfd3df"/></svg>hello@velahabitat.com</div>
  <div class="abs contact" style="left:702px">
    <svg width="10" height="10" viewBox="0 0 10 10"><path d="M2 0l2 2.5-1.2 1.3a6 6 0 003.4 3.4L7.5 6 10 8l-1.5 2C4 10 0 6 0 1.5z" fill="#cfd3df"/></svg>(555) 014 220 3318</div>
  <div class="abs socials"><span><i></i></span><span class="on"><i></i></span><span><i></i></span><span><i></i></span><span style="border-right:1px solid #26305a"><i></i></span></div>
</header>

<header class="site-header">
  <div class="abs brand"><span class="mark"></span>Vela Habitat</div>
  <nav class="abs nav"><span class="active">Home</span><span>About Us</span><span>Listing</span><span>Property</span><span>Selling</span><span>Buying</span><span>Blogs</span><span>Contact Us</span></nav>
  <svg class="abs nav-search" width="14" height="14" viewBox="0 0 14 14"><circle cx="6" cy="6" r="4.5" fill="none" stroke="#ff5a1f" stroke-width="2"/><path d="M9.5 9.5L13 13" stroke="#ff5a1f" stroke-width="2"/></svg>
</header>

<section class="hero" role="img" aria-label="Modern living room with glass wall overlooking a garden">
  <div class="abs floor"></div>
  <div class="abs search-tabs"><span class="on"><i></i></span><span><i></i></span><span><i></i></span><span><i></i></span></div>
  <div class="abs search-panel">
    <div class="abs select" style="left:22px;width:194px">Property</div>
    <div class="abs select" style="left:246px;width:186px">Country</div>
    <div class="abs select" style="left:456px;width:194px">State</div>
    <div class="abs select" style="left:674px;width:194px">City</div>
    <div class="abs range" style="left:22px;width:194px">Price :<span class="val">0 - 990000 $</span><div class="track"></div></div>
    <div class="abs range" style="left:246px;width:186px">Area :<span class="val">0 - 100000 ft</span><div class="track"></div></div>
    <div class="abs range" style="left:456px;width:194px">Bathrooms:<span class="val">0 - 2</span><div class="track"></div></div>
    <div class="abs range" style="left:674px;width:194px">Bedrooms:<span class="val">0 - 5</span><div class="track"></div></div>
    <div class="abs btn-search"><svg width="10" height="10" viewBox="0 0 14 14"><circle cx="6" cy="6" r="4.5" fill="none" stroke="#fff" stroke-width="2"/><path d="M9.5 9.5L13 13" stroke="#fff" stroke-width="2"/></svg>SEARCH NOW</div>
  </div>
</section>

<section class="categories">
  <div class="abs cat" style="left:156px"><div class="icon"><svg width="30" height="26" viewBox="0 0 30 26"><path d="M15 2L2 13h4v11h7v-7h4v7h7V13h4z" fill="#b9bcc4"/></svg></div><h3>Residential</h3><div class="bar"></div><p>Lorem ipsum dolor sit amet, consectetur adipiscing elit, sed do eiusmod tempor incididunt ut.</p><a>Read more &#8250;</a></div>
  <div class="abs cat featured" style="left:384px"><div class="icon"><svg width="22" height="30" viewBox="0 0 22 30"><rect x="1" y="1" width="20" height="28" fill="#fff"/><g fill="#101a3d"><rect x="5" y="5" width="4" height="4"/><rect x="13" y="5" width="4" height="4"/><rect x="5" y="12" width="4" height="4"/><rect x="13" y="12" width="4" height="4"/><rect x="8" y="20" width="6" height="9"/></g></svg></div><h3>Apartment</h3><div class="bar"></div><p>Lorem ipsum dolor sit amet, consectetur adipiscing elit, sed do eiusmod tempor incididunt ut.</p><a>Read more &#8250;</a></div>
  <div class="abs cat" style="left:612px"><div class="icon"><svg width="24" height="30" viewBox="0 0 24 30"><path d="M12 1L3 13h5l-6 8h8v8h4v-8h8l-6-8h5z" fill="#b9bcc4"/></svg></div><h3>Land</h3><div class="bar"></div><p>Lorem ipsum dolor sit amet, consectetur adipiscing elit, sed do eiusmod tempor incididunt ut.</p><a>Read more &#8250;</a></div>
  <div class="abs cat" style="left:840px"><div class="icon"><svg width="30" height="26" viewBox="0 0 30 26"><path d="M2 25V10l8 5V10l8 5V2h6v23z" fill="#b9bcc4"/></svg></div><h3>Commercial</h3><div class="bar"></div><p>Lorem ipsum dolor sit amet, consectetur adipiscing elit, sed do eiusmod tempor incididunt ut.</p><a>Read more &#8250;</a></div>
</section>

<section class="welcome">
  <div class="abs photo" role="img" aria-label="Bright living room with white corner sofa and framed artwork"></div>
  <h2 class="abs">Welcome to <em>Vela Habitat</em>, your first choice for Costa del Sol property!</h2>
  <p class="abs">Look at our Latest listed properties and check out the facilities on them. We have already sold more than 5,000 Homes and we are still going at very good pace. We would love you to look into these properties.</p>
  <div class="abs features">
    <span><svg width="16" height="16" viewBox="0 0 16 16"><path d="M8 0l3 3H9v4h4V5l3 3-3 3V9H9v4h2l-3 3-3-3h2V9H3v2L0 8l3-3v2h4V3H5z" fill="#ff5a1f"/></svg>570sq. ft</span>
    <span><svg width="20" height="14" viewBox="0 0 20 14"><path d="M0 2h2v6h18v6h-2v-3H2v3H0zM3 4h6v3H3zM10 4h8a2 2 0 012 2v1H10z" fill="#ff5a1f"/></svg>4 Bedroom</span>
    <span><svg width="18" height="14" viewBox="0 0 18 14"><path d="M0 6h18v2a5 5 0 01-5 5H5a5 5 0 01-5-5zM3 0h3v5H3z" fill="#ff5a1f"/></svg>3 Bath</span>
  </div>
  <div class="abs explore">Explore more &#8250;</div>
</section>

<section class="featured-sec">
  <h2 class="abs sec-title">Featured <em>Property</em></h2>
  <div class="abs title-line"></div>
  <div class="abs arrows">
    <svg width="22" height="10" viewBox="0 0 22 10"><path d="M21 5H2M6 1L2 5l4 4" fill="none" stroke="#bbb" stroke-width="1.5"/></svg>
    <svg width="22" height="10" viewBox="0 0 22 10"><path d="M1 5h19M16 1l4 4-4 4" fill="none" stroke="#ff5a1f" stroke-width="1.5"/></svg>
  </div>
  <div class="abs prop" style="left:156px">
    <div class="photo" role="img" aria-label="Villa with pool at dusk" style="background:linear-gradient(180deg,#6fa0d8 0%,#a9c4e4 45%,#c7a27a 75%,#5e7f95 100%)"></div>
    <div class="tag" style="background:#3fae49">Rent</div>
    <h4>Sol Tower, Estepona</h4><div class="price">$990,985</div>
    <p>Lorem ipsum dolor sit amet, consectetur adipiscing elit, sed do eiusmod tempor incididunt ut.</p>
    <ul><li>1650 Sq Ft</li><li>Swimming Pool</li><li>Bathroom</li><li>Kitchen</li></ul>
  </div>
  <div class="abs prop raised" style="left:459px">
    <div class="photo" role="img" aria-label="Stone house with garden" style="background:linear-gradient(180deg,#8aa6c4 0%,#9a8f80 50%,#5d7a3c 100%)"></div>
    <div class="tag" style="background:#e02b2b">Sell</div>
    <h4>Sol Tower, Estepona</h4><div class="price">$129,985</div>
    <p>Lorem ipsum dolor sit amet, consectetur adipiscing elit, sed do eiusmod tempor incididunt ut.</p>
    <ul><li>1650 Sq Ft</li><li>Swimming Pool</li><li>Bathroom</li><li>Kitchen</li></ul>
  </div>
  <div class="abs prop" style="left:764px">
    <div class="photo" role="img" aria-label="Resort pool among palm trees at sunset" style="background:linear-gradient(180deg,#d69a4a 0%,#8f8a4a 45%,#4c7a3a 70%,#3c8fb0 100%)"></div>
    <div class="tag" style="background:#2b8fe0">Buy</div>
    <h4>Sol Tower, Estepona</h4><div class="price">$247,456</div>
    <p>Lorem ipsum dolor sit amet, consectetur adipiscing elit, sed do eiusmod tempor incididunt ut.</p>
    <ul><li>1650 Sq Ft</li><li>Swimming Pool</li><li>Bathroom</li><li>Kitchen</li></ul>
  </div>
  <div class="abs btn-view">View All &nbsp;&#8250;</div>
</section>

<section class="stats">
  <div class="abs stat" style="left:155px"><svg width="34" height="30" viewBox="0 0 30 26"><path d="M15 2L2 13h4v11h7v-7h4v7h7V13h4z" fill="#ff5a1f"/></svg><div class="u"></div><small>Residential</small><b>3000</b></div>
  <div class="abs stat-div" style="left:369px"></div>
  <div class="abs stat" style="left:383px"><svg width="24" height="30" viewBox="0 0 22 30"><rect x="1" y="1" width="20" height="28" fill="none" stroke="#ff5a1f" stroke-width="2.5"/><g fill="#ff5a1f"><rect x="5" y="5" width="4" height="4"/><rect x="13" y="5" width="4" height="4"/><rect x="5" y="12" width="4" height="4"/><rect x="13" y="12" width="4" height="4"/><rect x="8" y="20" width="6" height="9"/></g></svg><div class="u"></div><small>Apartments</small><b>1050</b></div>
  <div class="abs stat-div" style="left:597px"></div>
  <div class="abs stat" style="left:611px"><svg width="34" height="30" viewBox="0 0 30 26"><path d="M2 25V10l8 5V10l8 5V2h6v23z" fill="#ff5a1f"/></svg><div class="u"></div><small>Commercial</small><b>750</b></div>
  <div class="abs stat-div" style="left:825px"></div>
  <div class="abs stat" style="left:840px"><svg width="30" height="28" viewBox="0 0 30 28"><path d="M15 27L3 15A7 7 0 0115 5a7 7 0 0112 10z" fill="#ff5a1f"/></svg><div class="u"></div><small>Clients</small><b>450</b></div>
</section>

<section class="work">
  <h2 class="abs sec-title">Our <em>Work</em></h2>
  <p class="abs sub">There are many variations of passages of Lorem Ipsum available, but the majority have suffered alteration in some form, by injected humour, or randomised words.</p>
  <div class="abs filters"><span>All</span><span class="on">Living Room</span><span>Kitchen</span><span>Garage</span><span>Bedroom</span></div>
  <div class="abs tile" style="left:0;top:208px;background:linear-gradient(135deg,#8a3a2a,#d8d6d2 60%,#f1f0ee)" role="img" aria-label="Living room with brick wall and white sofa"></div>
  <div class="abs tile" style="left:300px;top:208px;background:linear-gradient(160deg,#7d756b,#b9aea0 55%,#4a3a30)" role="img" aria-label="Modern bedroom with grey walls"></div>
  <div class="abs tile active" style="left:600px;top:208px;background:linear-gradient(180deg,#f3f3f3,#dedede)" role="img" aria-label="White minimal lounge with sofa"></div>
  <div class="abs tile" style="left:900px;top:208px;background:linear-gradient(160deg,#b96a40,#e9e4dc 50%,#c9c2b6)" role="img" aria-label="Lounge with fireplace and artwork"></div>
  <div class="abs tile" style="left:0;top:408px;background:linear-gradient(180deg,#a58d6a,#d9d4c8 55%,#3ea0c8)" role="img" aria-label="Thatched villa with swimming pool"></div>
  <div class="abs tile" style="left:300px;top:408px;background:linear-gradient(180deg,#8fb0d0,#c9c8c0 50%,#4f7a35)" role="img" aria-label="Country house with garden"></div>
  <div class="abs tile" style="left:600px;top:408px;background:linear-gradient(180deg,#e0d3bd,#c8b08a 60%,#8c6e4a)" role="img" aria-label="Classic living room with chandelier"></div>
  <div class="abs tile" style="left:900px;top:408px;background:linear-gradient(160deg,#5f7e43,#e6e3de 50%,#aaa59d)" role="img" aria-label="Open lounge with garden view"></div>
</section>

<section class="blogs">
  <h2 class="abs sec-title">Latest <em>Blogs</em></h2>
  <div class="abs post-img" style="left:156px;background:linear-gradient(180deg,#f2f2f2,#d9d6d0)" role="img" aria-label="White modern kitchen"></div>
  <div class="abs post-date" style="left:170px">05</div>
  <div class="abs post-text" style="left:384px"><h4>Don't be an architecture of building, be the architecture of life.</h4><div class="d">06th Of May</div><p>The first contracts have been signed in HOUSE, which will host many exclusive brands from Brazil and all over the World. Nordvik Corp, which has purchased 2 towers from...</p><a>Read more &#8250;</a></div>
  <div class="abs post-img" style="left:612px;background:linear-gradient(180deg,#e9e7e3,#cfc6b8 70%,#8c6a48)" role="img" aria-label="Bright lounge interior"></div>
  <div class="abs post-date" style="left:626px">08</div>
  <div class="abs post-text" style="left:840px"><h4>Don't be an architecture of building, be the architecture of life.</h4><div class="d">06th Of May</div><p>The first contracts have been signed in HOUSE, which will host many exclusive brands from Brazil and all over the World. Nordvik Corp, which has purchased 2 towers from...</p><a>Read more &#8250;</a></div>
</section>

<section class="cta">
  <svg width="760" height="112" viewBox="0 0 760 112"><polygon points="0,0 760,0 690,112 0,112" fill="#ff5a1f"/></svg>
  <h3 class="abs">Looking to sell your home?</h3>
  <p class="abs">Lorem ipsum dolor sit amet, consecteturin ligula convallis.</p>
  <div class="abs btn btn-start">Get Started</div>
  <div class="abs btn btn-contact">Contact Us</div>
</section>

<section class="contact" role="img" aria-label="Villa terrace at night">
  <div class="abs panel">
    <h4>Drop Us a Message!</h4><div class="rule"></div>
    <div class="addr">48 Paseo del Mar<br>Marbella - 29601<br>Spain</div>
    <h5>Contact Info</h5>
    <div class="call">Call: 555-014-7782</div>
    <div class="mail">info@velahabitat.com</div>
    <h5>Get Social</h5>
    <div class="soc"><i></i><i style="background:#d44a3a"></i><i style="background:#3ba3e0"></i><i style="background:#2a6fcf"></i><i style="background:#1a72b0"></i></div>
  </div>
  <div class="abs form">
    <label style="left:14px;top:78px">Name</label>
    <div class="field" style="left:14px;top:97px;width:201px;height:32px"></div>
    <label style="left:240px;top:78px">Email</label>
    <div class="field" style="left:240px;top:97px;width:203px;height:32px"></div>
    <label style="left:14px;top:143px">Message</label>
    <div class="field" style="left:14px;top:164px;width:429px;height:78px"></div>
    <div class="note">If you need to add attachments to the message please <b>click here &#8250;</b></div>
    <div class="btn-send"><svg width="10" height="10" viewBox="0 0 10 10"><path d="M0 4L10 0 7 10 5 6z" fill="#fff"/></svg>Send</div>
  </div>
</section>

<footer class="site-footer">
  <div class="abs copy">Copyright 2016 &copy; Vela Habitat</div>
  <div class="abs links">Copyright | Privacy &amp; Cookies Policy | Terms &amp; Conditions</div>
  <div class="abs to-top"><svg width="12" height="12" viewBox="0 0 12 12"><path d="M6 11V2M2 6l4-4 4 4" fill="none" stroke="#fff" stroke-width="2"/></svg></div>
</footer>

</body>
</html>
```